Website Design Brief – B2B Industrial Engineering Company

DO NOT CONTACT ME PRIVATELY. ANY INQUIRES WILL BE IGNORED.

1. Industry & Company Background

We are a Swiss B2B engineering and manufacturing company operating in the fields of:
• Industrial air technology (Lufttechnik)
• Metal fabrication and plant construction (Metallbau / Anlagebau)
• Design, fabrication, installation, maintenance, and servicing of:
• Spray booths / paint booths
• Extraction and ventilation systems
• Filtration and environmentally efficient air-handling systems

We plan, build, manufacture, sell, install, and maintain these systems.
Most systems are custom-built in-house (metalwork, apparatus construction, air technology), tailored to customer requirements rather than relying only on standard components.

We are a family-run business with a strong focus on:
• Swiss quality
• Long-term experience
• Reliability and engineering competence
• Environmental efficiency
• Apprenticeship training (we train apprentices in our workshop)

2. Goal of the New Website

The new website should be a modernized evolution of our existing site, not a complete reinvention.

Key objectives:
• Look more modern, fresh, and dynamic
• Clearly communicate our experience, quality, and values
• Emphasize Swiss engineering, tradition, and reliability
• Feel professional and trustworthy, not flashy
• Be clean, uncluttered, and highly structured
• Encourage visitors to submit an inquiry or contact us

The website should feel confident and industrial-premium, with a strong focus on clarity and usability.

3. Overall Design Direction

Visual Style
• Modern industrial design
• Clean layouts with strong structure
• Clear visual hierarchy
• Balanced use of whitespace
• Calm, confident, engineering-focused look

Layout Principles (Important)
• Use clearly separated sections
• Avoid overlapping elements
• Avoid overly complex or experimental layouts
• Prefer grid-based, structured compositions
• Each section should have a clear start and end
• Designs should translate well into standard web layouts without reliance on floating or layered effects

Motion & Media
• A video header on the homepage is strongly desired
• Industrial footage, workshop, fabrication, systems in operation, or environmental technology
• Subtle animations are welcome (e.g., fades, simple transitions)
• Avoid heavy parallax or effects that depend on overlapping elements

4. Target Audience
• Industrial and B2B clients
• Engineers, facility managers, workshop owners
• Decision-makers looking for reliable long-term partners
• Customers who value custom solutions, quality, and service

5. Reference Website

Existing website (content & structure reference):
https://www.glanzhallenwerk.ch

This site:
• Provides existing branding, colors, and tone
• Is the baseline for content and structure
• Should be visually improved, simplified, and modernized

6. Pages to Design (Initial Phase – 5 Pages)

Please design 5 key pages, based on the existing website structure:
1. Home
• Video header
• Clear value proposition
• Overview of services
• Trust elements (experience, Swiss quality, family business)
• Strong call-to-action (Contact / Request Quote)
2. Company / About Us
• Company history
• Values and philosophy
• Swiss quality and tradition
• Family business
• Apprenticeship training and workshop
3. Services / Solutions
• Planning
• Manufacturing
• Installation
• Maintenance & service
• Custom systems vs standard components
4. Products / Systems
• Spray booths
• Extraction systems
• Filtration and air technology
• Modular but clearly structured sections
5. Contact
• Contact form
• Company details
• Location
• Clear inquiry-focused layout

7. Functional Requirements

Must Have
• Contact form
• Newsletter signup
• Cookie consent (EU / GDPR compliant)
• Privacy policy and legal pages (EU data protection)
• Clear navigation structure
• PDF catalog download area (well organized)

Must NOT Have
• No search feature
• No cluttered mega-menus
• No hidden or confusing navigation

8. Future Expansion (Phase Two – Not Required Now)

Designs should allow future expansion, including:
• Multi-language support (English, French, Italian)
• Optional webshop integration
• Expanded product catalog
• Additional service pages

These features do not need to be designed now, but the layout should be flexible enough to support them later.

9. Colors & Branding
• Use colors similar to the existing website
• Industrial, neutral tones preferred
• Accents should feel technical and professional
• Avoid trendy or overly bright color palettes

10. Tone & Messaging

The design should communicate:
• Experience
• Precision
• Trust
• Environmental responsibility
• Custom engineering capability
• Long-term partnership mindset

The overall impression should be:

“A modern Swiss engineering company with deep experience, strong values, and reliable solutions.”

11. Final Notes for Designers
• Focus on clarity, structure, and usability
• Designs should be realistic to implement with standard web layouts
• Avoid designs that rely on overlapping elements or complex layering
• Think in terms of clean sections, strong grids, and clear content flow
• The primary conversion goal is customer inquiries

Target Market(s)

The target market is B2B industrial customers, not consumers.

Industry/Entity Type

B2B industrial engineering and manufacturing (air technology, metal construction, plant engineering).

Number of Pages Required

5+ page

Requirements
Must have
• Clean structured layout, clear B2B positioning, video header, strong inquiry CTA, contact form, GDPR compliance, PDF downloads.
Nice to have
• Newsletter signup, multilingual-ready structure, future webshop support.
Should not have
• Search feature, overlapping elements, complex layered layouts, cluttered navigation.

```html
<!DOCTYPE html>
<html lang="en">
<head>
<meta charset="utf-8">
<title>Services – Glanzhallen</title>
<link href="https://fonts.googleapis.com/css2?family=Inter:wght@400;500;600;700;800&display=swap" rel="stylesheet">
<style>
:root{
  --red:#e0332a;
  --dark:#111214;
  --dark-2:#1a1b1e;
  --ink:#17181b;
  --muted:#5d6168;
  --line:#e3e4e7;
  --soft:#f3f4f6;
  --white:#ffffff;
  --photo-a:#aeb6c0;
  --photo-b:#6f7a88;
}
*{box-sizing:border-box;margin:0;padding:0}
html,body{width:1200px;height:3284px;overflow:hidden}
body{font-family:"Inter",sans-serif;color:var(--ink);background:var(--white);font-size:11px;line-height:1.5}
.wrap{width:800px;margin:0 auto}
.label{color:var(--red);font-size:8px;font-weight:700;letter-spacing:.12em;text-transform:uppercase}

/* Hero */
.hero{height:260px;background:radial-gradient(ellipse at 20% 60%,#3a1410 0,transparent 45%),radial-gradient(ellipse at 85% 40%,#3a1410 0,transparent 40%),var(--dark);color:var(--white)}
.nav{height:44px;display:flex;align-items:center;justify-content:space-between;padding:0 120px;border-bottom:1px solid #26272b}
.brand{font-weight:800;font-size:12px;letter-spacing:.08em;color:var(--white)}
.nav ul{display:flex;gap:18px;list-style:none;align-items:center;font-size:9px;color:#c9cbd0}
.nav li.on{background:#2c2d31;padding:4px 9px;border-radius:3px;color:#fff}
.btn{display:inline-block;background:var(--red);color:#fff;font-weight:600;font-size:9px;padding:6px 12px;border-radius:3px}
.hero-body{padding:70px 0 0 340px}
.pill{display:inline-block;border:1px solid #3a3b40;border-radius:20px;font-size:8px;color:#c9cbd0;padding:4px 12px}
.hero h1{font-size:36px;font-weight:800;margin:12px 0 8px;letter-spacing:-.01em}
.hero p{font-size:10px;color:#b8bbc1;width:460px}

/* Approach */
.approach{height:472px;padding-top:94px}
.approach .wrap{display:grid;grid-template-columns:1fr 1fr;gap:40px}
.approach h2{font-size:20px;font-weight:700;margin:6px 0 12px}
.approach p{color:var(--muted);font-size:9.5px;margin-bottom:10px}
.checks{list-style:none;display:grid;gap:7px}
.checks li{border:1px solid var(--line);border-radius:4px;padding:7px 10px;font-size:9px;display:flex;gap:8px;align-items:center;background:var(--soft)}
.checks svg{flex:none}

/* Services */
.services{height:1460px;background:var(--soft);padding-top:50px}
.center{text-align:center}
.services h2,.support h2{font-size:22px;font-weight:700;margin-top:4px}
.rows{margin-top:36px;display:grid;gap:30px}
.row{display:grid;grid-template-columns:1fr 1fr;gap:36px;align-items:center;height:236px}
.card{background:var(--white);border-radius:6px;padding:16px 20px;height:100%}
.card h3{font-size:14px;font-weight:700;display:flex;align-items:center;gap:9px;margin-bottom:8px}
.ico{width:24px;height:24px;border:1px solid var(--line);border-radius:4px;display:grid;place-items:center}
.card p{color:var(--muted);font-size:9px;margin-bottom:8px}
.bullets{list-style:none;display:grid;gap:4px}
.bullets li{font-size:9px;color:#3b3e44;padding-left:12px;position:relative}
.bullets li:before{content:"";position:absolute;left:0;top:6px;width:4px;height:4px;background:var(--red);border-radius:50%}
.photo{height:210px;border-radius:6px;background:linear-gradient(135deg,var(--photo-a),var(--photo-b))}

/* Support */
.support{height:308px;padding-top:50px}
.support .sub{color:var(--muted);font-size:9.5px;margin-top:6px}
.plans{width:540px;margin:24px auto 0;display:grid;grid-template-columns:1fr 1fr;gap:16px}
.plan{border:1px solid var(--line);border-radius:5px;padding:14px 16px;background:var(--soft);text-align:left}
.plan h4{font-size:11px;margin-bottom:8px}

/* CTA */
.cta{height:220px;background:var(--dark-2);color:#fff;text-align:center;padding-top:66px}
.cta h2{font-size:22px;font-weight:700}
.cta p{color:#b8bbc1;font-size:9.5px;margin:6px 0 16px}

/* Footer */
.footer{height:510px;background:var(--dark);color:#9ea1a7;padding-top:70px;font-size:8.5px}
.footer .wrap{width:960px;display:grid;grid-template-columns:1.4fr 1fr 1fr 1fr;gap:30px}
.footer h5{color:#fff;font-size:9px;margin-bottom:8px}
.footer ul{list-style:none;display:grid;gap:4px}
.footer .brand{margin-bottom:8px}

/* Cookie */
.cookie{height:54px;background:var(--white);border-top:1px solid var(--line);display:flex;align-items:center;justify-content:space-between;padding:0 120px;font-size:8px;color:var(--muted)}
.cookie b{color:var(--ink);display:block;font-size:9px}
.cookie .acts{display:flex;gap:6px}
.ghost{border:1px solid var(--line);padding:5px 10px;border-radius:3px;color:var(--ink);font-size:8.5px}
</style>
</head>
<body>

<header class="hero">
  <nav class="nav">
    <div class="brand">GLANZHALLEN</div>
    <ul><li>Home</li><li>About</li><li class="on">Services</li><li>Products</li><li><span class="btn">Contact</span></li></ul>
  </nav>
  <div class="hero-body">
    <span class="pill">← Back to Homepage</span>
    <h1>Complete Service Solutions</h1>
    <p>From initial planning to ongoing maintenance, we handle every aspect of your industrial air technology requirements.</p>
  </div>
</header>

<section class="approach">
  <div class="wrap">
    <div>
      <div class="label">Full Service Approach</div>
      <h2>Engineering-Driven Solutions</h2>
      <p>We don't just sell equipment. We work with you as a partner to understand your unique operational requirements, challenges, and long-term goals.</p>
      <p>Our integrated approach ensures seamless delivery from concept through commissioning, with ongoing support tailored to your needs.</p>
    </div>
    <ul class="checks">
      <li><svg width="10" height="10" viewBox="0 0 10 10"><path d="M1.5 5.2l2.3 2.3 4.7-5" stroke="#e0332a" stroke-width="1.5" fill="none"/></svg>Detailed needs assessment</li>
      <li><svg width="10" height="10" viewBox="0 0 10 10"><path d="M1.5 5.2l2.3 2.3 4.7-5" stroke="#e0332a" stroke-width="1.5" fill="none"/></svg>Custom system design</li>
      <li><svg width="10" height="10" viewBox="0 0 10 10"><path d="M1.5 5.2l2.3 2.3 4.7-5" stroke="#e0332a" stroke-width="1.5" fill="none"/></svg>In-house manufacturing</li>
      <li><svg width="10" height="10" viewBox="0 0 10 10"><path d="M1.5 5.2l2.3 2.3 4.7-5" stroke="#e0332a" stroke-width="1.5" fill="none"/></svg>Professional installation</li>
      <li><svg width="10" height="10" viewBox="0 0 10 10"><path d="M1.5 5.2l2.3 2.3 4.7-5" stroke="#e0332a" stroke-width="1.5" fill="none"/></svg>Comprehensive training</li>
      <li><svg width="10" height="10" viewBox="0 0 10 10"><path d="M1.5 5.2l2.3 2.3 4.7-5" stroke="#e0332a" stroke-width="1.5" fill="none"/></svg>24/7 technical support</li>
    </ul>
  </div>
</section>

<section class="services">
  <div class="wrap">
    <div class="center"><div class="label">Our Services</div><h2>Comprehensive Service Suite</h2></div>
    <div class="rows">
      <div class="row">
        <div class="card">
          <h3><span class="ico"><svg width="12" height="12" viewBox="0 0 12 12"><path d="M2 10h8M3 8l5-5 1.5 1.5-5 5H3z" stroke="#17181b" fill="none"/></svg></span>Planning &amp; Design</h3>
          <p>Every successful project starts with thorough planning. Our engineering team analyzes your facility, assesses the process requirements and develops custom designs optimized for efficiency and reliability.</p>
          <ul class="bullets"><li>Facility walkthrough and assessment</li><li>Requirement analysis and workflow evaluation</li><li>CAD design and technical specifications</li><li>Compliance verification and permits</li><li>Cost-benefit analysis and timeline</li><li>Environmental impact assessment</li></ul>
        </div>
        <div class="photo" role="img" aria-label="Engineers reviewing system plans at a workstation"></div>
      </div>
      <div class="row">
        <div class="photo" role="img" aria-label="Workers fabricating metal components in the workshop"></div>
        <div class="card">
          <h3><span class="ico"><svg width="12" height="12" viewBox="0 0 12 12"><circle cx="6" cy="6" r="2.2" stroke="#17181b" fill="none"/><path d="M6 1v2M6 9v2M1 6h2M9 6h2" stroke="#17181b"/></svg></span>Manufacturing</h3>
          <p>Our in-house fabrication capabilities allow us to manufacture custom components with precision and quality control. We combine traditional Swiss metalworking with modern technology for superior results.</p>
          <ul class="bullets"><li>Metal fabrication and welding</li><li>Apparatus and apparatus construction</li><li>Filter system assembly</li><li>Ductwork and fan production</li><li>Quality testing and inspection</li><li>Made-to-order specifications</li></ul>
        </div>
      </div>
      <div class="row">
        <div class="card">
          <h3><span class="ico"><svg width="12" height="12" viewBox="0 0 12 12"><path d="M2 10l5-5M7 2l3 3-2 2-3-3z" stroke="#17181b" fill="none"/></svg></span>Installation &amp; Commissioning</h3>
          <p>Our specialized installation team manages the entire setup process from site preparation and equipment placement to testing, startup and operator training. We ensure seamless integration with your existing operations.</p>
          <ul class="bullets"><li>Site preparation and logistics</li><li>Equipment positioning and alignment</li><li>Electrical and mechanical connections</li><li>System testing and validation</li><li>Operator training and documentation</li><li>Performance validation</li></ul>
        </div>
        <div class="photo" role="img" aria-label="Installation team assembling a booth on site"></div>
      </div>
      <div class="row">
        <div class="photo" role="img" aria-label="Technicians servicing an air handling unit"></div>
        <div class="card">
          <h3><span class="ico"><svg width="12" height="12" viewBox="0 0 12 12"><path d="M6 1.5l4 1.5v3c0 2.5-2 4-4 4.5C4 10 2 8.5 2 6V3z" stroke="#17181b" fill="none"/></svg></span>Maintenance &amp; Service</h3>
          <p>Long-term reliability requires regular care. We provide comprehensive maintenance programs, emergency repairs, component replacement and performance tuning to maximize system lifespan and minimize downtime.</p>
          <ul class="bullets"><li>Preventive maintenance plans</li><li>Filter replacement and disposal</li><li>Component repair and replacement</li><li>Emergency breakdown service</li><li>System performance optimization</li><li>Extended warranty options</li></ul>
        </div>
      </div>
      <div class="row">
        <div class="card">
          <h3><span class="ico"><svg width="12" height="12" viewBox="0 0 12 12"><path d="M7 1L3 7h3l-1 4 4-6H6z" stroke="#17181b" fill="none"/></svg></span>Efficiency Retrofits</h3>
          <p>Extend the life of existing systems while improving operational costs. Our retrofit programs upgrade aging equipment with modern energy-efficient technology, advanced filtration and smart controls.</p>
          <ul class="bullets"><li>Energy audit and analysis</li><li>Heat recovery upgrades</li><li>LED lighting upgrades</li><li>Advanced fan controllers</li><li>Modern filtration technology</li><li>Significant cost and energy savings</li></ul>
        </div>
        <div class="photo" role="img" aria-label="Modernized spray booth interior with bright lighting"></div>
      </div>
    </div>
  </div>
</section>

<section class="support center">
  <h2>Support &amp; Warranties</h2>
  <p class="sub">We stand behind our work with comprehensive support programs and industry-leading warranties.</p>
  <div class="plans">
    <div class="plan"><h4>Standard Warranty</h4><ul class="bullets"><li>Up to 5 years on select products</li><li>Manufacturing defect coverage</li><li>Parts and labor included</li><li>Optional extension available</li></ul></div>
    <div class="plan"><h4>24/7 Technical Support</h4><ul class="bullets"><li>Emergency hotline for critical issues</li><li>Remote diagnostics and troubleshooting</li><li>Rapid on-site service available</li><li>Spare parts inventory ready</li></ul></div>
  </div>
</section>

<section class="cta">
  <h2>Ready to Optimize Your Operations?</h2>
  <p>Contact our team for a detailed consultation on custom service solutions tailored to your facility.</p>
  <span class="btn">Request Consultation</span>
</section>

<footer class="footer">
  <div class="wrap">
    <div><div class="brand">GLANZHALLEN</div><p>Swiss engineering excellence in industrial air technology and metal fabrication since decades of practice.</p></div>
    <div><h5>Company</h5><ul><li>About Us</li><li>Services</li><li>Products</li><li>Contact</li></ul></div>
    <div><h5>Solutions</h5><ul><li>Spray Booths</li><li>Extraction Systems</li><li>Air Filtration</li><li>Technical Support</li></ul></div>
    <div><h5>Contact</h5><ul><li>+41 44 512 73 90</li><li>info@glanzhallenwerk.ch</li><li>Switzerland</li></ul></div>
  </div>
</footer>

<div class="cookie">
  <div><b>Cookie Consent</b>We use cookies to enhance your browsing experience and analyze site traffic. By clicking Accept, you consent to our use of cookies.</div>
  <div class="acts"><span class="ghost">Reject</span><span class="btn">Accept</span></div>
</div>

</body>
</html>
```